Private Maths Tuition Flyer based in London

I am opening up a new Maths tuition centre in North West London. The flyer will be delivered to over 8,000 homes within the immediate vicinity. The design should be suitable to be printed on an A5 sheet and read in a portrait orientation.

The flyer should include the following:

The headline statement should be "Private Maths Tuition"

Secondary headline statement is the following "GCSE, A-Levels, 11 Plus exams"

Some of service offerings/selling points are:

- Free first session
- Monthly Feedback reports
- Free support outside of sessions
- Clear Target grades
- Personalised Lesson plans
- Tangible Results

Another statement that should be featured is "Book your free session by visiting www.lernova.co.uk" or something similar to that.

"Contact Details:
020 4719 8263
enquiries@lernova.co.uk"

"Address:
Kelbridge Business and Innovation Centre
Ashvale Court
Wrenfield Road
HA4 9QD"

Attached you'll see a logo which should be included and also a map of where we are. I am open to new images for the map if you guys have any, rather than a screen shot from google maps but it should be clear to see.

I would like the content above to be displayed in a clear and concise manner that is easy to read. You have creative license on where this information should be displayed and where the images should be but on the whole it should look aesthetically pleasing on the eye.

Target Market(s)

Students, Parents. Parents who want maths tutors.

Industry/Entity Type

Tutoring

Font styles to use
Sans Serif

Requirements
Must have
• *logo*
• Private Maths Tuition
• GCSE, A-Levels, 11 Plus exams
• - Free first session
• - Monthly Feedback reports
• - Free support outside of sessions
• - Clear Target grades
• - Personalised Lesson plans
• - Tangible Results
• Book your free session by visiting www.lernova.co.uk" or something similar to that.
• Contact Details:
• 020 4719 8263
• enquiries@lernova.co.uk
• Address (*with map*):
• Kelbridge Business and Innovation Centre
• Ashvale Court
• Wrenfield Road
• HA4 9QD
Nice to have
• similar colour scheme as the logo. creative background design.

```html
<!DOCTYPE html>
<html lang="en">
<head>
<meta charset="utf-8">
<title>Lernova – Private Maths Tuition Flyer</title>
<link href="https://fonts.googleapis.com/css2?family=Arimo:wght@400;700&display=swap" rel="stylesheet">
<style>
  :root {
    --brand-blue: #1756a9;
    --brand-orange: #f26f21;
    --brand-green: #8dc63f;
    --ink: #3a3a3a;
    --rule: #9a9a9a;
    --paper: #ffffff;
    --backdrop: #1e1e1e;
  }
  * { margin: 0; padding: 0; box-sizing: border-box; }
  html, body {
    width: 1200px; height: 1200px; overflow: hidden;
    background: var(--backdrop);
    font-family: "Arimo", Arial, sans-serif;
  }
  .flyer {
    position: absolute; left: 186px; top: 20px;
    width: 828px; height: 1160px;
    background: var(--paper);
    overflow: hidden;
  }
  .colour-band { position: absolute; top: 0; left: 0; width: 100%; height: 26px; display: flex; }
  .colour-band span:nth-child(1) { width: 341px; background: var(--brand-orange); }
  .colour-band span:nth-child(2) { width: 334px; background: var(--brand-blue); }
  .colour-band span:nth-child(3) { flex: 1; background: var(--brand-green); }

  .brand-name {
    position: absolute; left: 76px; top: 118px;
    display: flex; align-items: center; gap: 12px;
    font-size: 56px; font-weight: 400; color: var(--brand-orange); line-height: 1;
  }
  .brand-name .dot { width: 16px; height: 16px; border-radius: 50%; background: var(--brand-green); }

  .headline {
    position: absolute; left: 70px; top: 192px;
    font-size: 128px; font-weight: 700; color: var(--brand-blue);
    line-height: 122px; letter-spacing: -2px;
  }
  .headline-rule { position: absolute; left: 72px; top: 573px; width: 405px; height: 7px; background: var(--brand-green); }
  .subhead {
    position: absolute; left: 77px; top: 600px;
    font-size: 25px; font-weight: 700; color: var(--brand-orange);
  }

  .student-photo {
    position: absolute; left: 509px; top: 51px; width: 190px; height: 617px;
    background: linear-gradient(180deg, #e9d8cf 0%, #f1b3b8 30%, #8aa0bb 55%, #50627e 80%, #2b2b2b 100%);
    border-radius: 90px 90px 24px 24px;
  }

  .offer-tag {
    position: absolute; left: 72px; top: 668px; width: 229px; height: 36px;
    background: var(--brand-orange); color: #fff;
    font-size: 22px; font-weight: 700; padding-left: 18px; line-height: 36px;
  }
  .selling-points { position: absolute; left: 72px; top: 704px; width: 334px; list-style: none; }
  .selling-points li {
    height: 31px; line-height: 30px; font-size: 19px; color: var(--ink);
    border-bottom: 1px solid var(--rule); padding-left: 29px; position: relative;
  }
  .selling-points li::before {
    content: "★"; position: absolute; left: 8px; top: 0;
    color: var(--brand-orange); font-size: 13px;
  }

  .location-map {
    position: absolute; left: 446px; top: 672px; width: 308px; height: 372px;
    background: linear-gradient(160deg, #ece9e2 0%, #e4e1d8 55%, #d2e3bf 100%);
    border-top: 3px solid var(--brand-blue); border-bottom: 3px solid var(--brand-blue);
  }

  .contact-block { position: absolute; left: 77px; top: 902px; font-size: 16px; color: var(--ink); line-height: 20px; }
  .contact-block h3 { font-size: 16px; font-weight: 700; color: var(--brand-blue); }
  .address-block { position: absolute; left: 77px; top: 991px; font-size: 16px; color: var(--ink); line-height: 20.5px; }
  .address-block h3 { font-size: 16px; font-weight: 700; color: var(--brand-blue); }

  .booking-prompt {
    position: absolute; left: 275px; top: 1064px;
    font-size: 18px; color: var(--brand-blue);
  }
  .booking-button {
    position: absolute; left: 274px; top: 1093px; width: 274px; height: 67px;
    background: var(--brand-blue); color: #fff;
    font-size: 22px; font-weight: 700; text-align: center; line-height: 50px;
  }
</style>
</head>
<body>
  <main class="flyer">
    <div class="colour-band"><span></span><span></span><span></span></div>

    <div class="brand-name"><span>Lernova</span><span class="dot"></span></div>

    <h1 class="headline">Private<br>Maths<br>Tuition</h1>
    <div class="headline-rule"></div>
    <p class="subhead">GCSE, A-Levels, 11 Plus Exams</p>

    <div class="student-photo" role="img" aria-label="Photo of a smiling student holding a red folder"></div>

    <div class="offer-tag">Free first session</div>
    <ul class="selling-points">
      <li>Monthly Feedback reports</li>
      <li>Free support outside of sessions</li>
      <li>Clear Target grades</li>
      <li>Personalised Lesson plans</li>
      <li>Tangible Results</li>
    </ul>

    <div class="location-map" role="img" aria-label="Street map showing the location of the tuition centre"></div>

    <div class="contact-block">
      <h3>Contact Details:</h3>
      <p>020 4719 8263</p>
      <p>enquiries@lernova.co.uk</p>
    </div>

    <div class="address-block">
      <h3>Address:</h3>
      <p>Kelbridge Business and Innovation Centre</p>
      <p>Ashvale Court</p>
      <p>Wrenfield Road</p>
      <p>HA4 9QD</p>
    </div>

    <p class="booking-prompt">Book your free session by visiting</p>
    <div class="booking-button">www.lernova.co.uk</div>
  </main>
</body>
</html>
```